Consulting/Brand Licensing business needs business card

We need a business card created for our IP company, that also does consulting and brand licensing. We would like this card to be vague, as our other business' are in the cannabis industry and this is a non-cannabis touching entity. Perhaps something that hints vaguely at the industry without alerting or possibly offending the receiver.

Target Market(s)

CEOs/Key Decision Makers/Industry Leaders

Contact Information for Business Card

No address, simply list Seattle, WA. Phone: 206-555-0143. Name: Dario Lindqvist // email: Dario@velmarcoast.com

Colors

Designer to choose colors to be used in the design.

Requirements
Must have
• Logo, Name, Email, Phone number, "Consulting, Licensing and Branding Specialists"
Nice to have
• We would like this to be more professional than playful.

```html
<!DOCTYPE html>
<html lang="en">
<head>
<meta charset="utf-8">
<title>Velmar Coast, Inc — Business Card</title>
<link href="https://fonts.googleapis.com/css2?family=Open+Sans:wght@400;600;700&display=swap" rel="stylesheet">
<style>
  :root {
    --backdrop: #e8e8e9;
    --card: #222121;
    --accent: #e8542a;
    --emboss: #4d4a49;
    --emboss-light: #5a5756;
  }
  * { margin: 0; padding: 0; box-sizing: border-box; }
  html, body {
    width: 1200px;
    height: 800px;
    overflow: hidden;
    background: var(--backdrop);
    font-family: "Open Sans", Arial, sans-serif;
  }
  .canvas {
    position: relative;
    width: 1200px;
    height: 800px;
  }
  .card {
    position: absolute;
    width: 520px;
    height: 297px;
    background: var(--card);
    border-radius: 4px;
  }
  .card--front { left: 70px; top: 110px; }
  .card--back { left: 610px; top: 390px; }

  .brand-name {
    color: var(--accent);
    font-weight: 700;
    letter-spacing: 0.5px;
    white-space: nowrap;
  }

  /* Front */
  .front-lockup {
    position: absolute;
    left: 0; right: 0;
    top: 96px;
    text-align: center;
  }
  .front-lockup .brand-name { font-size: 40px; }
  .website {
    margin-top: 22px;
    color: var(--accent);
    font-size: 14px;
    font-weight: 400;
  }

  /* Back */
  .back-lockup {
    position: absolute;
    right: 32px;
    top: 40px;
    text-align: right;
  }
  .back-lockup .brand-name { font-size: 26px; }
  .tagline {
    margin-top: 6px;
    color: var(--emboss-light);
    font-size: 10px;
    font-weight: 600;
    letter-spacing: 0.3px;
  }
  .person {
    position: absolute;
    left: 40px;
    top: 118px;
  }
  .person-name {
    color: var(--emboss);
    font-size: 19px;
    font-weight: 700;
  }
  .person-title {
    color: var(--accent);
    font-size: 12px;
    font-weight: 700;
    margin-top: 1px;
  }
  .contacts {
    position: absolute;
    left: 40px;
    top: 200px;
    list-style: none;
  }
  .contact {
    display: flex;
    align-items: center;
    gap: 7px;
    color: var(--emboss);
    font-size: 12px;
    line-height: 21px;
  }
  .contact svg { width: 11px; height: 11px; fill: var(--accent); flex: none; }
</style>
</head>
<body>
<main class="canvas">

  <section class="card card--front" aria-label="Card front">
    <div class="front-lockup">
      <div class="brand-name">Velmar Coast, Inc</div>
      <div class="website">yourwebsite.com</div>
    </div>
  </section>

  <section class="card card--back" aria-label="Card back">
    <div class="back-lockup">
      <div class="brand-name">Velmar Coast, Inc</div>
      <div class="tagline">Consulting, Licensing and Branding Specialists</div>
    </div>

    <div class="person">
      <div class="person-name">Dario Lindqvist</div>
      <div class="person-title">Job Title</div>
    </div>

    <ul class="contacts">
      <li class="contact">
        <svg viewBox="0 0 12 12" aria-hidden="true"><path d="M1 3.5C1 2 2.5 1 6 1s5 1 5 2.5V5H8.5V3.8C8 3.5 7 3.3 6 3.3S4 3.5 3.5 3.8V5H1z"/><path d="M2.5 6h7l1 5h-9z"/></svg>
        206-555-0143
      </li>
      <li class="contact">
        <svg viewBox="0 0 12 12" aria-hidden="true"><path d="M0.5 2.5h11v7h-11z M1.5 3.2 6 6.6l4.5-3.4" stroke="#222121" stroke-width="0.9"/></svg>
        Dario@velmarcoast.com
      </li>
      <li class="contact">
        <svg viewBox="0 0 12 12" aria-hidden="true"><path d="M6 0.5a4 4 0 0 1 4 4c0 3-4 7-4 7s-4-4-4-7a4 4 0 0 1 4-4zm0 2.3a1.6 1.6 0 1 0 0 3.2 1.6 1.6 0 0 0 0-3.2z"/></svg>
        Seattle, WA.
      </li>
    </ul>
  </section>

</main>
</body>
</html>
```